Business Card Design EFTPOS Comparison site

At QuoteLark.com.au we are a free service that allows our customers to get up to five quotes from our panel of suppliers for a range of BUSINESS related products and services. These products include eftpos / credit card machines, bank accounts, insurance, signage,office furniture etc. basically anything that a small business would need.
The process is done in 3 steps; 1) register your enquiry 2) we source and provide the five cheapest quotes 3) then select the supplier of your choice,the process is simple QuoteLark and is FREE.
Please visit the soon to be revamped website to see our logo.
Target Market(s)
Small business operators
Industry/Entity Type
Small Business
Requirements
Must have
- Double Sided card

```html
<!DOCTYPE html>
<html lang="en">
<head>
<meta charset="utf-8">
<title>QuoteLark business card</title>
<link href="https://fonts.googleapis.com/css2?family=Ubuntu:wght@400;500;700&family=Didact+Gothic&display=swap" rel="stylesheet">
<style>
  :root{
    --bg:#efedea;
    --red:#d41f22;
    --red-deep:#d01c20;
    --orange:#e9921f;
    --orange-mid:#e2612a;
    --white:#ffffff;
    --logo:#e2612a;
    --web:#c8161c;
  }
  html,body{margin:0;padding:0;overflow:hidden;}
  body{width:1200px;height:1012px;background:var(--bg);position:relative;font-family:"Ubuntu",sans-serif;}
  .card{position:absolute;left:280px;width:640px;height:360px;border-radius:32px;overflow:hidden;}
  .card-front{top:140px;background:linear-gradient(90deg,var(--red) 0%,var(--red-deep) 30%,var(--orange-mid) 62%,var(--orange) 100%);}
  .card-back{top:528px;background:var(--white);}

  .logo-tab{position:absolute;left:0;top:108px;width:278px;height:142px;background:var(--white);border-radius:0 72px 72px 0;display:flex;align-items:center;}
  .logo-name{margin-left:26px;font-family:"Ubuntu",sans-serif;font-weight:700;font-size:38px;color:var(--logo);letter-spacing:-0.5px;}

  .steps{position:absolute;left:290px;top:136px;margin:0;padding:0;list-style:none;color:var(--white);font-size:11.5px;font-weight:700;}
  .steps li{display:flex;margin-bottom:14px;line-height:14px;}
  .steps .num{font-weight:400;width:31px;flex:none;}
  .steps .num::after{content:" |";}

  .swoosh{position:absolute;left:0;top:0;width:640px;height:360px;}

  .identity{position:absolute;left:220px;width:400px;top:40px;text-align:center;color:var(--white);}
  .identity .name{font-weight:700;font-size:21px;margin:0;}
  .identity .role{font-family:"Didact Gothic",sans-serif;font-size:18px;margin:2px 0 0;}

  .contact{position:absolute;color:var(--white);font-family:"Didact Gothic",sans-serif;font-size:17px;line-height:22px;}
  .label{position:absolute;color:var(--white);font-weight:700;font-size:22px;}
  .rule{position:absolute;background:var(--white);}

  .web{position:absolute;left:28px;bottom:18px;color:var(--web);font-weight:700;font-size:17px;}
</style>
</head>
<body>
  <section class="card card-front">
    <div class="logo-tab"><span class="logo-name">QuoteLark</span></div>
    <ol class="steps">
      <li><span class="num">01</span><span>Register your enquiry</span></li>
      <li><span class="num">02</span><span>We Source and provide the five cheapest quotes</span></li>
      <li><span class="num">03</span><span>Select the supplier of your choice, the process<br>is simple QuoteLark and is FREE.</span></li>
    </ol>
  </section>

  <section class="card card-back">
    <svg class="swoosh" viewBox="0 0 640 360" aria-hidden="true">
      <defs>
        <linearGradient id="swooshFill" x1="0" y1="0" x2="1" y2="0">
          <stop offset="0" stop-color="#e8721f"/>
          <stop offset="0.45" stop-color="#dc3d24"/>
          <stop offset="1" stop-color="#d41c20"/>
        </linearGradient>
      </defs>
      <path d="M198,0 L640,0 L640,346 L232,310 Q168,302 170,252 L195,20 Q197,2 198,0 Z" fill="#f3b58f" opacity="0.6"/>
      <path d="M205,0 L640,0 L640,340 L236,302 Q176,294 178,248 L201,20 Q203,2 205,0 Z" fill="#e3552a"/>
      <path d="M213,0 L640,0 L640,334 L242,296 Q186,288 188,244 L208,20 Q211,2 213,0 Z" fill="url(#swooshFill)"/>
    </svg>

    <div class="identity">
      <p class="name">Daniel James Porter</p>
      <p class="role">assistant manager</p>
    </div>

    <span class="rule" style="left:246px;top:134px;width:2px;height:140px;"></span>
    <span class="label" style="left:234px;top:154px;">A</span>
    <div class="contact" style="left:258px;top:130px;">Unit 8, 22-26 Hollis Court,<br>Brendale, Queensland 4500, Australia.</div>
    <span class="rule" style="left:248px;top:176px;width:350px;height:2px;"></span>

    <span class="label" style="left:234px;top:198px;">P</span>
    <div class="contact" style="left:258px;top:196px;">02 5550 1842</div>
    <span class="rule" style="left:248px;top:220px;width:120px;height:2px;"></span>

    <span class="rule" style="left:446px;top:178px;width:2px;height:44px;"></span>
    <span class="label" style="left:436px;top:198px;">F</span>
    <div class="contact" style="left:460px;top:196px;">02 5550 7736</div>
    <span class="rule" style="left:448px;top:220px;width:120px;height:2px;"></span>

    <span class="label" style="left:234px;top:242px;">E</span>
    <div class="contact" style="left:258px;top:240px;">DanielJamesPorter@quotelark.com</div>
    <span class="rule" style="left:248px;top:264px;width:326px;height:2px;"></span>

    <span class="web">www.quotelark.com.au</span>
  </section>
</body>
</html>
```